Wrap on a Tarvo truck with a topper the focus is Roofing.
The company name Dorwick Construction, I have attached a business card.
I have attached their current bill board in town that should have all the info you need to design the wrap. I have also attached picture of the truck

```html
<!DOCTYPE html>
<html lang="en">
<head>
<meta charset="utf-8">
<title>Dorwick Construction – Truck Wrap Layouts</title>
<link rel="stylesheet" href="https://fonts.googleapis.com/css2?family=Roboto+Condensed:wght@500;700&family=Roboto+Slab:wght@800&family=Archivo:wght@800&family=Nunito:wght@700&display=swap">
<style>
  :root {
    --canvas: #f4f4f2;
    --body-white: #ffffff;
    --wrap-black: #141414;
    --band-white: #f2f2f2;
    --ink: #111111;
    --outline: #d6d6d6;
    --badge-grey: #9a9a9a;
  }
  * { margin: 0; padding: 0; box-sizing: border-box; }
  html, body { width: 1200px; height: 1200px; overflow: hidden; background: var(--canvas); }
  .sheet {
    width: 1200px; height: 1200px;
    display: flex; flex-direction: column; justify-content: space-around;
    padding: 40px 50px;
  }
  .wrap-layout { width: 1100px; height: 520px; display: block; }
  .panel-cab { fill: var(--body-white); stroke: var(--outline); stroke-width: 2; }
  .panel-topper { fill: var(--wrap-black); }
  .panel-band { fill: var(--band-white); }
  .panel-rule { fill: var(--wrap-black); }
  .panel-shingle { fill: url(#shingleTone); }
  .company-name { font-family: "Roboto Condensed", sans-serif; font-weight: 500; font-size: 46px; fill: #ffffff; }
  .services { font-family: "Nunito", sans-serif; font-weight: 700; font-size: 24px; fill: #ffffff; letter-spacing: 2px; }
  .phone { font-family: "Archivo", sans-serif; font-weight: 800; font-size: 40px; fill: var(--ink); letter-spacing: 3px; }
  .tagline { font-family: "Roboto Slab", serif; font-weight: 800; font-size: 28px; fill: var(--ink); }
  .stripe-text { font-family: "Roboto Slab", serif; font-weight: 800; font-size: 22px; fill: #ffffff; }
  .social-mark { fill: var(--ink); }
  .social-name { font-family: "Roboto Condensed", sans-serif; font-weight: 700; font-size: 13px; fill: var(--ink); }
  .model-badge { font-family: "Roboto Condensed", sans-serif; font-weight: 700; font-size: 9px; fill: var(--badge-grey); }
  .brand-mark { font-family: "Roboto Condensed", sans-serif; font-weight: 700; fill: var(--ink); }
</style>
</head>
<body>
<main class="sheet">

  <svg class="wrap-layout layout-large-mark" viewBox="0 0 1100 520" aria-label="Dorwick Construction wrap layout, large mark">
    <defs>
      <linearGradient id="shingleTone" x1="0" y1="0" x2="0" y2="1">
        <stop offset="0" stop-color="#948f89"/>
        <stop offset="1" stop-color="#76716b"/>
      </linearGradient>
    </defs>
    <rect class="panel-cab" x="2" y="110" width="588" height="370" rx="28"/>
    <rect class="panel-topper" x="580" y="20" width="518" height="230"/>
    <text class="company-name" x="839" y="110" text-anchor="middle" textLength="470" lengthAdjust="spacingAndGlyphs">DORWICK CONSTRUCTION</text>
    <text class="services" x="839" y="190" text-anchor="middle">roofing-siding-gutters</text>
    <rect class="panel-band" x="580" y="250" width="518" height="54"/>
    <text class="phone" x="839" y="292" text-anchor="middle">555.014.2290</text>
    <rect class="panel-rule" x="580" y="304" width="518" height="8"/>
    <rect class="panel-shingle" x="580" y="312" width="518" height="168" role="img" aria-label="Shingle roof texture with dormer window illustration"/>
    <rect class="panel-rule" x="2" y="420" width="578" height="42"/>
    <text class="stripe-text" x="200" y="449" text-anchor="middle">Licensed &amp; Insured Local</text>
    <circle class="social-mark" cx="40" cy="255" r="6"/>
    <text class="social-name" x="52" y="260">Palbook</text>
    <text class="social-name" x="40" y="280">Pixgram</text>
    <text class="tagline" x="200" y="300" text-anchor="middle">Storm</text>
    <text class="tagline" x="200" y="338" text-anchor="middle">Damage Experts</text>
    <text class="model-badge" x="140" y="360">TARVO HD</text>
    <text class="brand-mark" x="455" y="300" font-size="64" text-anchor="middle" textLength="220" lengthAdjust="spacingAndGlyphs">DORWICK</text>
  </svg>

  <svg class="wrap-layout layout-compact-mark" viewBox="0 0 1100 520" aria-label="Dorwick Construction wrap layout, compact mark">
    <rect class="panel-cab" x="2" y="110" width="588" height="370" rx="28"/>
    <rect class="panel-topper" x="580" y="20" width="518" height="230"/>
    <text class="company-name" x="839" y="110" text-anchor="middle" textLength="470" lengthAdjust="spacingAndGlyphs">DORWICK CONSTRUCTION</text>
    <text class="services" x="839" y="190" text-anchor="middle">roofing-siding-gutters</text>
    <rect class="panel-band" x="580" y="250" width="518" height="54"/>
    <text class="phone" x="839" y="292" text-anchor="middle">555.014.2290</text>
    <rect class="panel-rule" x="580" y="304" width="518" height="8"/>
    <rect class="panel-shingle" x="580" y="312" width="518" height="168" role="img" aria-label="Shingle roof texture with dormer window illustration"/>
    <rect class="panel-rule" x="2" y="420" width="578" height="42"/>
    <text class="stripe-text" x="200" y="449" text-anchor="middle">Licensed &amp; Insured Local</text>
    <circle class="social-mark" cx="40" cy="255" r="6"/>
    <text class="social-name" x="52" y="260">Palbook</text>
    <text class="social-name" x="40" y="280">Pixgram</text>
    <text class="tagline" x="200" y="300" text-anchor="middle">Storm</text>
    <text class="tagline" x="200" y="338" text-anchor="middle">Damage Experts</text>
    <text class="model-badge" x="140" y="360">TARVO HD</text>
    <text class="brand-mark" x="470" y="395" font-size="44" text-anchor="middle" textLength="170" lengthAdjust="spacingAndGlyphs">DORWICK</text>
  </svg>

</main>
</body>
</html>
```